Association qui souhaite améliorer l'accès aux personnes en situation de handicap

Nous sommes une association qui a pour objectif d'améliorer l'accessibilité, augmenter l'offre des activités réalisables dans notre région touristique.
Nous souhaitons réaliser un site internet afin de pouvoir communiquer sur notre association. Nous avons déjà conçu notre flyer sur Graphivolta. Nous souhaiterions une base graphique se rapportant à celui-ci. C'est possible de tout retravailler mais nous souhaitons tout de même retrouver la charte graphique ou code couleur du flyer.
Il nous faudrait quelques pages:
- 1 page : Acceuil / Présentation (Home), Il y aurait le descriptif de l'association, avec ses objectifs à +/- moyen terme
- 1 page : Nos réalisations, celle-ci présenterait les éléments que nous avons réalisés avec des zones de textes et des images classées chronologiquement au fur et à mesure des nouveautés
- 1 page : Media, comme la précédente, mais ou on pourrait voir ou lire sur les divers médias qui parlent de nous
- 1 page : Evenements : c'est une page pour présenter divers activités que nous allons organiser
- 1 page : Contact qui indique comment nous contacter et avec la présentation des 5 ou 6 membres du comité
- 1 link donate : qui arrive sur un formulaire de donnée que l'on pourra faire évoluer sur un système de payement par la suite. Cette bannière doit se retrouver sur toutes les pages
Il est nécessaire que se design puisse être transféré sur une lecture sur téléphone mobile
Target Market(s)
Personnes en situation de handicap
Industry/Entity Type
Associatif
Coding
Coded - Design and coding required
Number of Pages Required
5+ page

```html
<!DOCTYPE html>
<html lang="en">
<head>
<meta charset="utf-8">
<title>Openway Association</title>
<link href="https://fonts.googleapis.com/css2?family=Bebas+Neue&family=Raleway:wght@400;500;600&display=swap" rel="stylesheet">
<style>
:root{
  --red:#ea4a43;
  --deep-red:#c21d2a;
  --flame:#e03d1d;
  --blush:#fbeced;
  --ink:#333333;
  --text:#4a4a4a;
  --dark:#3b3b3b;
  --white:#ffffff;
  --line:#bdbdbd;
}
*{box-sizing:border-box;margin:0;padding:0}
html,body{width:1200px;height:4431px;overflow:hidden;background:var(--white)}
body{position:relative;font-family:'Raleway',sans-serif;color:var(--text)}
.heading,.nav a,.btn,.card-title,.item-title{font-family:'Bebas Neue',sans-serif;font-weight:400}
section,header,footer{position:absolute;left:0;width:1200px}
.abs{position:absolute}
.btn{position:absolute;display:flex;align-items:center;justify-content:center;background:var(--red);color:var(--white);font-size:23px;letter-spacing:.5px;width:178px;height:50px}
.btn-outline{background:transparent;border:2px solid var(--red);color:var(--red);font-size:18px;width:132px;height:52px}
.accent{color:var(--flame)}
.wordmark{display:flex;align-items:center;gap:10px;font-family:'Raleway',sans-serif;font-weight:600;font-size:22px;color:var(--deep-red)}
.wordmark .mark{width:30px;height:30px;background:var(--deep-red)}

/* header */
.site-header{top:0;height:107px;background:var(--white)}
.site-header .wordmark{position:absolute;left:74px;top:38px}
.nav{position:absolute;left:424px;top:42px;display:flex;gap:34px}
.nav a{font-size:22px;color:var(--ink);text-decoration:none}
.nav a.current{color:var(--red)}
.site-header .btn{left:975px;top:29px;width:151px;height:50px;font-size:24px}

/* hero */
.hero{top:107px;height:720px}
.hero-photo{position:absolute;left:0;top:0;width:1200px;height:641px;background:linear-gradient(100deg,#3a3f33 0%,#5d6a45 35%,#8a9a63 65%,#b5bd8c 100%)}
.hero-panel{position:absolute;left:0;top:182px;width:705px;height:222px;background:rgba(40,40,40,.72)}
.hero-title{position:absolute;left:74px;top:200px;font-size:66px;color:var(--white);letter-spacing:.5px}
.hero-sub{position:absolute;left:74px;top:283px;font-size:29px;line-height:38px;color:var(--white);width:600px}
.hero .btn{left:74px;top:374px}
.dots{position:absolute;left:74px;top:582px;display:flex;gap:7px}
.dots i{width:10px;height:10px;background:var(--flame)}
.dots i:first-child{background:var(--white)}

/* welcome */
.welcome{top:748px;height:627px}
.welcome-mark{position:absolute;left:45px;top:120px;width:540px;height:430px;display:flex;align-items:center;justify-content:center}
.welcome-mark .wordmark{font-size:42px}
.welcome-mark .mark{width:56px;height:56px}
.welcome .heading{position:absolute;left:615px;top:122px;font-size:50px;line-height:50px;color:var(--ink)}
.welcome p{position:absolute;left:615px;top:240px;width:520px;font-size:17px;line-height:30.5px}
.welcome .btn{left:615px;top:486px}

/* objectives */
.objectives{top:1350px;height:665px}
.objectives .heading{position:absolute;left:74px;top:100px;font-size:52px;color:var(--ink)}
.objectives .intro{position:absolute;left:74px;top:170px;width:515px;font-size:17px;line-height:25px}
.checklist{position:absolute;left:74px;top:265px;list-style:none}
.checklist li{display:flex;align-items:center;gap:16px;height:40.6px;font-size:17px;color:var(--ink)}
.checklist svg{flex:none}
.objectives .btn{left:74px;top:524px}
.objectives-photo{position:absolute;left:615px;top:108px;width:585px;height:480px;background:linear-gradient(135deg,#f0f0f0,#c9cbcf 60%,#a9aeb6)}

/* achievements */
.achievements{top:2015px;height:650px}
.achievements .heading{position:absolute;left:0;width:1200px;top:65px;text-align:center;font-size:54px;color:var(--ink)}
.card{position:absolute;top:151px;width:328px;height:440px}
.card-photo{position:absolute;left:0;top:0;width:328px;height:251px}
.card-body{position:absolute;left:19px;top:200px;width:290px;height:187px;background:var(--white);box-shadow:0 4px 14px rgba(0,0,0,.12);clip-path:polygon(0 14px,100% 0,100% 100%,0 100%)}
.card-title{position:absolute;left:35px;top:264px;font-size:26px;color:var(--flame)}
.card-text{position:absolute;left:35px;top:300px;width:270px;font-size:16.5px;line-height:25px}
.card .btn{left:19px;top:381px}

/* media & events */
.news{top:2665px;height:645px}
.news .heading{position:absolute;top:92px;font-size:50px;color:var(--ink)}
.news .btn-outline{top:92px}
.divider{position:absolute;left:602px;top:92px;width:2px;height:452px;background:var(--red)}
.media-item{position:absolute;left:74px;width:465px}
.media-item + .media-item{}
.item-title{font-size:25px;color:var(--flame);line-height:31px}
.item-text{margin-top:10px;font-size:16.5px;line-height:25px}
.rule{position:absolute;left:74px;width:465px;height:1px;background:var(--line)}
.event{position:absolute;left:636px;width:490px}
.event-photo{position:absolute;left:0;top:0;width:175px;height:146px;border:3px solid var(--white);box-shadow:0 2px 6px rgba(0,0,0,.18)}
.event-body{position:absolute;left:208px;top:0;width:282px}

/* contact */
.contact{top:3310px;height:690px}
.contact-photo{position:absolute;left:0;top:97px;width:586px;height:530px;background:linear-gradient(120deg,#f3cfd1,#e9b3b4 45%,#d4a39a)}
.contact .heading{position:absolute;left:615px;top:95px;font-size:50px;color:var(--ink)}
.contact .intro{position:absolute;left:615px;top:163px;width:520px;font-size:17px;line-height:25px}
.field{position:absolute;border:1px solid #9c9c9c;background:var(--white);font-size:16.5px;color:var(--ink);padding:0 16px;display:flex;align-items:center}
.field.msg{align-items:flex-start;padding-top:18px}
.contact .btn{left:615px;top:513px}

/* donate */
.donate{top:3960px;height:232px}
.donate .heading{position:absolute;left:227px;top:80px;font-size:50px;color:var(--white)}
.donate p{position:absolute;left:227px;top:140px;width:520px;font-size:17px;line-height:25px;color:var(--white)}
.donate .btn{left:798px;top:106px;width:177px;font-size:24px}

/* footer */
.site-footer{top:4192px;height:239px;background:var(--red);color:var(--white)}
.site-footer .wordmark{position:absolute;left:74px;top:52px;color:var(--white);font-size:24px}
.site-footer .wordmark .mark{background:var(--white)}
.copy{position:absolute;left:74px;top:148px;font-size:15px;line-height:25px}
.foot-title{position:absolute;top:38px;font-family:'Bebas Neue',sans-serif;font-size:25px}
.links{position:absolute;left:402px;top:80px;list-style:none;font-size:14.5px;line-height:27.5px}
.news-input{position:absolute;left:602px;top:83px;width:223px;height:42px;background:var(--white);color:var(--ink);font-size:15px;display:flex;align-items:center;padding-left:12px}
.subscribe{position:absolute;left:602px;top:133px;width:223px;height:44px;background:#f4c6c4;color:var(--red);font-family:'Bebas Neue',sans-serif;font-size:21px;display:flex;align-items:center;justify-content:center}
.social{position:absolute;left:901px;top:86px;display:flex;gap:22px}
.social i{width:26px;height:26px;background:var(--white)}
</style>
</head>
<body>

<header class="site-header">
  <div class="wordmark"><span class="mark"></span>Openway Association</div>
  <nav class="nav">
    <a class="current" href="#">Home</a>
    <a href="#">Our Achievements</a>
    <a href="#">Media</a>
    <a href="#">Events</a>
    <a href="#">Contact</a>
  </nav>
  <a class="btn" href="#">Donate Now</a>
</header>

<section class="hero">
  <div class="hero-photo" role="img" aria-label="Hand gently touching tall grass beside a wheelchair wheel in a meadow"></div>
  <svg class="abs" style="left:0;top:0" width="1200" height="720" viewBox="0 0 1200 720">
    <polygon points="0,474 660,404 0,518" fill="var(--flame)"/>
    <polygon points="0,711 1200,641 1200,720 0,720" fill="var(--white)"/>
  </svg>
  <div class="hero-panel"></div>
  <h1 class="heading hero-title">Openway Association</h1>
  <p class="hero-sub">We are an association whose objective is to improve accessibility.</p>
  <a class="btn" href="#">Read More</a>
  <div class="dots"><i></i><i></i><i></i><i></i></div>
</section>

<section class="welcome">
  <div class="welcome-mark"><div class="wordmark"><span class="mark"></span>Openway</div></div>
  <h2 class="heading">Welcome to<br><span class="accent">Openway Association</span></h2>
  <p>Sed ut perspiciatis unde omnis iste natus error sit voluptatem accusantium doloremque laudantium, totam rem aperiam, eaque ipsa quae ab illo inventore veritatis et quasi architecto beatae vitae dicta sunt explicabo. Nemo enim ipsam voluptatem quia voluptas sit aspernatur aut odit aut fugit, sed quia consequuntur magni dolores eos qui ratione voluptatem sequi.</p>
  <a class="btn" href="#">Read More</a>
</section>

<section class="objectives">
  <svg class="abs" style="left:0;top:0" width="1200" height="665" viewBox="0 0 1200 665">
    <polygon points="0,25 690,25 1200,0 1200,665 0,665" fill="var(--blush)"/>
  </svg>
  <h2 class="heading">Medium-Term <span class="accent">Objectives</span></h2>
  <p class="intro">Sed ut perspiciatis unde omnis iste natus error sit voluptatem accusantium doloremque laudantium, totam rem aperiam, eaque ipsa quae ab illo inventore.</p>
  <ul class="checklist">
    <li><svg width="17" height="17" viewBox="0 0 17 17"><circle cx="8.5" cy="8.5" r="8.5" fill="var(--flame)"/><path d="M4.5 8.7l2.8 2.8 5.2-5.3" stroke="#fff" stroke-width="2" fill="none"/></svg>Sed ut perspiciatis unde omnis iste natus error sit.</li>
    <li><svg width="17" height="17" viewBox="0 0 17 17"><circle cx="8.5" cy="8.5" r="8.5" fill="var(--flame)"/><path d="M4.5 8.7l2.8 2.8 5.2-5.3" stroke="#fff" stroke-width="2" fill="none"/></svg>Voluptatem accusantium doloremque laudantium</li>
    <li><svg width="17" height="17" viewBox="0 0 17 17"><circle cx="8.5" cy="8.5" r="8.5" fill="var(--flame)"/><path d="M4.5 8.7l2.8 2.8 5.2-5.3" stroke="#fff" stroke-width="2" fill="none"/></svg>Ttam rem aperiam, eaque ipsa quae.</li>
    <li><svg width="17" height="17" viewBox="0 0 17 17"><circle cx="8.5" cy="8.5" r="8.5" fill="var(--flame)"/><path d="M4.5 8.7l2.8 2.8 5.2-5.3" stroke="#fff" stroke-width="2" fill="none"/></svg>Ab illo inventore.</li>
    <li><svg width="17" height="17" viewBox="0 0 17 17"><circle cx="8.5" cy="8.5" r="8.5" fill="var(--flame)"/><path d="M4.5 8.7l2.8 2.8 5.2-5.3" stroke="#fff" stroke-width="2" fill="none"/></svg>Nemo enim ipsam voluptatem quia voluptas sit.</li>
    <li><svg width="17" height="17" viewBox="0 0 17 17"><circle cx="8.5" cy="8.5" r="8.5" fill="var(--flame)"/><path d="M4.5 8.7l2.8 2.8 5.2-5.3" stroke="#fff" stroke-width="2" fill="none"/></svg>Aspernatur aut odit aut fugit, sed quia consequuntu.</li>
  </ul>
  <a class="btn" href="#">Read More</a>
  <div class="objectives-photo" role="img" aria-label="Two hands sheltering a small wheelchair accessibility figure"></div>
  <svg class="abs" style="left:615px;top:470px" width="585" height="150" viewBox="0 0 585 150">
    <polygon points="0,0 585,90 585,150" fill="var(--flame)"/>
    <polygon points="0,0 0,150 585,150" fill="var(--blush)"/>
  </svg>
</section>

<section class="achievements">
  <h2 class="heading">Our <span class="accent">Achievements</span></h2>
  <article class="card" style="left:74px">
    <div class="card-photo" role="img" aria-label="Group of friends raising joined hands outdoors, one in a wheelchair" style="background:linear-gradient(180deg,#e4e8ea,#b7c0b3 60%,#8d9a78)"></div>
    <div class="card-body"></div>
    <h3 class="card-title">Excepteur sint occa</h3>
    <p class="card-text">Sed ut perspiciatis unde omnis iste natus error sit volu pta tem accusantium.</p>
    <a class="btn" href="#">Read More</a>
  </article>
  <article class="card" style="left:437px">
    <div class="card-photo" role="img" aria-label="Smiling man pushing an older man in a wheelchair through a city square" style="background:linear-gradient(180deg,#8f9690,#6a6a5e 55%,#4d4a42)"></div>
    <div class="card-body"></div>
    <h3 class="card-title">Excepteur sint occa</h3>
    <p class="card-text">Sed ut perspiciatis unde omnis iste natus error sit volu pta tem accusantium.</p>
    <a class="btn" href="#">Read More</a>
  </article>
  <article class="card" style="left:798px">
    <div class="card-photo" role="img" aria-label="Man with a white cane walking along a green park path" style="background:linear-gradient(180deg,#7c9160,#a6ad8b 50%,#6f7a52)"></div>
    <div class="card-body"></div>
    <h3 class="card-title">Excepteur sint occa</h3>
    <p class="card-text">Sed ut perspiciatis unde omnis iste natus error sit volu pta tem accusantium.</p>
    <a class="btn" href="#">Read More</a>
  </article>
</section>

<section class="news">
  <svg class="abs" style="left:0;top:0" width="1200" height="645" viewBox="0 0 1200 645">
    <polygon points="0,0 1200,0 1200,645 690,645 0,645" fill="var(--blush)"/>
  </svg>
  <h2 class="heading" style="left:74px">Media</h2>
  <a class="btn btn-outline" href="#" style="left:434px">View All</a>
  <div class="media-item" style="top:182px"><h3 class="item-title">Excepteur sint occaecat cupidatat non</h3><p class="item-text">Sed ut perspiciatis unde omnis iste natus error sit volu ptatem accusantium doloremque laudan.</p></div>
  <div class="rule" style="top:286px"></div>
  <div class="media-item" style="top:324px"><h3 class="item-title">Excepteur sint occaecat cupidatat non</h3><p class="item-text">Sed ut perspiciatis unde omnis iste natus error sit volu ptatem accusantium doloremque laudan.</p></div>
  <div class="rule" style="top:428px"></div>
  <div class="media-item" style="top:465px"><h3 class="item-title">Excepteur sint occaecat cupidatat non</h3><p class="item-text">Sed ut perspiciatis unde omnis iste natus error sit volu ptatem accusantium doloremque laudan.</p></div>
  <div class="divider"></div>
  <h2 class="heading" style="left:632px">Events</h2>
  <a class="btn btn-outline" href="#" style="left:994px">View All</a>
  <div class="event" style="top:182px">
    <div class="event-photo" role="img" aria-label="Large group in red costumes gathered outdoors at a festive event" style="background:linear-gradient(160deg,#9a7a62,#b9302c 55%,#7d2a25)"></div>
    <div class="event-body"><h3 class="item-title">Excepteur sint occaecat cupidatat non</h3><p class="item-text">Sed ut perspiciatis unde omnis iste natus error sit voluptatem accusantium doloremque lauda ntium, totam rem.</p></div>
  </div>
  <div class="event" style="top:390px">
    <div class="event-photo" role="img" aria-label="Man in a red shirt seated in an adapted vehicle at an outdoor activity" style="background:linear-gradient(160deg,#7f8f6a,#b24a4a 55%,#3f3f3f)"></div>
    <div class="event-body"><h3 class="item-title">Excepteur sint occaecat cupidatat non</h3><p class="item-text">Sed ut perspiciatis unde omnis iste natus error sit voluptatem accusantium doloremque lauda ntium, totam rem.</p></div>
  </div>
</section>

<section class="contact">
  <svg class="abs" style="left:0;top:0" width="1200" height="60" viewBox="0 0 1200 60">
    <polygon points="0,0 690,0 1200,42 1200,0" fill="var(--blush)"/>
  </svg>
  <div class="contact-photo" role="img" aria-label="Young man with a tablet and smiling young woman sharing a fist bump"></div>
  <svg class="abs" style="left:0;top:520px" width="586" height="120" viewBox="0 0 586 120">
    <polygon points="0,0 586,0 586,17 0,110" fill="var(--white)" opacity="0"/>
    <polygon points="0,70 586,15 586,20 0,120" fill="var(--flame)"/>
    <polygon points="586,20 586,120 0,120" fill="var(--white)"/>
  </svg>
  <h2 class="heading">Contact <span class="accent">Us</span></h2>
  <p class="intro">Sed ut perspiciatis unde omnis iste natus error sit voluptatem accusantium doloremque laudantium, totam.</p>
  <div class="field" style="left:615px;top:223px;width:248px;height:53px">First Name</div>
  <div class="field" style="left:878px;top:223px;width:248px;height:53px">Last Name</div>
  <div class="field" style="left:615px;top:293px;width:248px;height:53px">Phone No</div>
  <div class="field" style="left:878px;top:293px;width:248px;height:53px">Email Address</div>
  <div class="field msg" style="left:615px;top:363px;width:511px;height:135px">Message</div>
  <a class="btn" href="#">Read More</a>
</section>

<section class="donate">
  <svg class="abs" style="left:0;top:0" width="1200" height="232" viewBox="0 0 1200 232">
    <polygon points="0,37 690,37 1200,0 1200,232 0,232" fill="var(--dark)"/>
  </svg>
  <h2 class="heading">Donate</h2>
  <p>Sed ut perspiciatis unde omnis iste natus error sit voluptatem accusantium doloremque laudantium, totam.</p>
  <a class="btn" href="#">Donate Now</a>
</section>

<footer class="site-footer">
  <div class="wordmark"><span class="mark"></span>Openway Association</div>
  <p class="copy">© Copyright 2022 CompanyName<br>All Rights Reserved</p>
  <h4 class="foot-title" style="left:402px">Quick Links</h4>
  <ul class="links"><li>Home</li><li>Our achievements</li><li>Media</li><li>Events</li><li>Contact</li></ul>
  <h4 class="foot-title" style="left:602px">Newletter</h4>
  <div class="news-input">Email Address</div>
  <div class="subscribe">Subscribe</div>
  <h4 class="foot-title" style="left:901px">Follow Us</h4>
  <div class="social"><i></i><i></i><i></i><i></i></div>
</footer>

</body>
</html>
```